Flyer-Design für ambulanten Pflegedienst
Zielgruppe
Wir sind ein ambulanter Pflegedienst im Raum Rostock und Gnoien. Patienten werden in der Häuslichkeit versorgt.
Aufgabenstellung
Überschrift: Der Pflegedienst im Herzen von Rostock
Der Faltflyer sollte darüber aufklären, dass Leistungen der Behandlungspflege von der Krankenkasse übernommen werden. Dazu zählt die Medikamentengabe das anziehen von Kompressionsstrümpfen und die Insulininjektion. Darüber soll in dem Flyer aufgeklärt werden. Die Texte können den Postkarten Flyern entnommen werden.
Der Flyer sollte einen hochwertigen Eindruck machen und
nicht zu viel Text enthalten. Da wir zwei ambulante Pflegedienste betreiben, soll der Flyer im Impressum mit zwei verschiedenen Adressen und zwei verschiedenen Logos auf der Rückseite erstellt werden.
Der Slogan des Flyers sollte sein: Der Pflegedienst im Herzen von Rostock.

```html
<!DOCTYPE html>
<html lang="de">
<head>
<meta charset="utf-8">
<title>Faltflyer Pflegehaus Warnow</title>
<link href="https://fonts.googleapis.com/css2?family=Patrick+Hand+SC&family=Quicksand:wght@400;500;700&display=swap" rel="stylesheet">
<style>
:root{
  --bg:#e9eaec;
  --paper:#f7f8fa;
  --green:#93d27e;
  --green-strong:#74c35a;
  --blue:#1f6db5;
  --blue-dark:#17589a;
  --orange:#f3a53c;
  --ink:#1d5fa8;
  --gray:#5c6f86;
}
*{margin:0;padding:0;box-sizing:border-box}
html,body{width:900px;height:1200px;overflow:hidden;background:var(--bg)}
body{font-family:"Quicksand",sans-serif;color:var(--ink);position:relative}
.sheet{position:absolute;left:40px;width:820px;height:580px;display:grid;grid-template-columns:repeat(3,1fr);background:var(--paper);box-shadow:0 6px 18px rgba(0,0,0,.12)}
.sheet--outside{top:12px}
.sheet--inside{top:608px;border-top:4px solid var(--blue)}
.panel{position:relative;overflow:hidden}
.panel + .panel{border-left:1px solid rgba(0,0,0,.06)}
.hand{font-family:"Patrick Hand SC",cursive;letter-spacing:.5px}
.pill{display:inline-block;border-radius:14px;color:#fff;font-family:"Patrick Hand SC",cursive;white-space:nowrap}
.pill--green{background:var(--green)}
.pill--orange{background:var(--orange)}
.pill--blue{background:var(--blue)}
.photo{position:absolute}
.badge{position:absolute;width:92px;height:92px;border-radius:50%;background:var(--orange);border:3px solid #fbd7a6;color:#fff;font-size:9.5px;line-height:1.2;text-align:center;display:flex;align-items:center;justify-content:center;padding:10px;font-weight:500}
.checks{list-style:none}
.checks li{position:relative;padding-left:17px;font-size:10.5px;line-height:14.2px;color:var(--ink)}
.checks li::before{content:"";position:absolute;left:2px;top:2px;width:5px;height:8px;border:solid var(--green-strong);border-width:0 2.5px 2.5px 0;transform:rotate(40deg)}
.brand{display:flex;align-items:center;gap:8px;font-weight:700;white-space:nowrap}
.brand__dot{width:30px;height:30px;border-radius:50%;flex:none}
.contact{list-style:none;font-size:10px;line-height:1.3}
.contact li{display:flex;gap:9px;align-items:flex-start;margin-bottom:7px}
.contact svg{flex:none;margin-top:1px}
.url{font-size:11px;font-weight:700;padding:5px 14px}

/* outside */
.care__photo{left:0;top:0;width:100%;height:175px;background:linear-gradient(135deg,#f2f2f2,#e5e3df 45%,#d9cbb6);border-bottom-right-radius:140px 60px}
.care__badge{left:170px;top:120px}
.care__title{position:absolute;left:18px;top:218px;font-size:20px;padding:2px 16px}
.care__lead{position:absolute;left:18px;top:252px;right:14px;font-size:11px;font-weight:700;line-height:1.25}
.care__list{position:absolute;left:18px;top:290px;z-index:1}
.care__photo2{left:190px;top:445px;width:83px;height:135px;background:linear-gradient(160deg,#f4efe6,#e9d3b4);border-top-left-radius:60px}

.contact-panel{background:var(--green);color:#fff}
.contact-panel .contact{color:#fff}
.contact-panel .brand{color:#fff;font-size:17px}
.contact-panel .brand__dot{background:#fff}
.contact-panel__main{position:absolute;left:38px;top:56px;right:20px}
.contact-panel__main .brand{margin-bottom:26px}
.contact-panel .url{margin-top:6px}
.contact-panel__branch{position:absolute;left:38px;top:318px;right:20px}
.contact-panel__branch .brand{margin-bottom:6px}
.contact-panel__tag{font-size:9px;margin:-2px 0 20px 38px;font-weight:500}

.cover__brand{position:absolute;top:28px;left:0;right:0;justify-content:center;color:var(--green-strong);font-size:21px}
.cover__brand .brand__dot{background:var(--blue)}
.cover__photo{left:38px;top:90px;width:210px;height:210px;border-radius:50%;background:linear-gradient(140deg,#cfd9bf,#f0e6dc 50%,#a9c1d8)}
.cover__badge{left:172px;top:72px;width:86px;height:86px;font-size:9px}
.cover__band{position:absolute;left:0;bottom:0;width:100%;height:330px}
.cover__title{position:absolute;left:16px;right:16px;top:395px;color:#fff;font-size:25px;line-height:1.05;text-align:center}
.cover__url{position:absolute;left:50%;transform:translateX(-50%);top:470px}

/* inside */
.insulin__photo{left:0;top:0;width:100%;height:180px;background:linear-gradient(135deg,#f3f5f7,#cfd9e8 45%,#4f5a66);border-bottom-right-radius:130px 80px}
.section-title{position:absolute;font-size:19px;padding:2px 16px}
.insulin__title{left:22px;top:192px}
.insulin__text{position:absolute;left:22px;right:16px;top:228px;font-size:9.5px;line-height:1.3;color:var(--gray)}
.insulin__text h3,.stockings__text h3{font-size:10.5px;color:var(--ink);margin:0 0 4px}
.insulin__text p{margin-bottom:7px}
.insulin__text .checks{margin-bottom:7px}
.insulin__text .checks li{font-size:9.5px;line-height:12.4px;color:var(--gray);margin-bottom:2px}

.promise__brand{position:absolute;top:40px;left:0;right:0;justify-content:center;color:var(--green-strong);font-size:21px}
.promise__brand .brand__dot{background:var(--blue)}
.promise__slogan{position:absolute;top:112px;left:0;right:0;display:flex;flex-direction:column;align-items:center;gap:5px}
.promise__slogan .pill{font-size:17px;padding:1px 16px}
.promise__phone{position:absolute;top:228px;left:50%;transform:translateX(-50%);font-family:"Quicksand",sans-serif;font-weight:700;font-size:17px;padding:6px 16px;display:flex;align-items:center;gap:8px}
.promise__phone small{font-size:9px}
.promise__photo{left:0;bottom:0;width:100%;height:275px;background:linear-gradient(180deg,rgba(247,248,250,1),#f1e3d8 45%,#dcc0ac)}

.stockings__photo{left:0;top:0;width:100%;height:215px;background:linear-gradient(140deg,#fbf4ee,#f0d4bd 55%,#e3b79a);border-bottom-left-radius:130px 80px}
.stockings__title{left:18px;top:228px}
.stockings__text{position:absolute;left:22px;right:18px;top:272px;font-size:10px;line-height:1.35;color:var(--gray)}
.stockings__text p{margin-bottom:12px}
.stockings__text .checks{margin-bottom:14px}
.stockings__text .checks li{font-size:10px;line-height:13px;color:var(--gray);margin-bottom:3px}
</style>
</head>
<body>

<section class="sheet sheet--outside">
  <article class="panel care">
    <div class="photo care__photo" role="img" aria-label="Foto: Pflasterrolle, Spritze, Stethoskop und Mullbinden"></div>
    <div class="badge care__badge">nach den neuesten, fachlichen Erkenntnissen</div>
    <h2 class="pill pill--green care__title">Behandlungspflege</h2>
    <p class="care__lead">Folgende Leistungen gehören unter anderem zur Behandlungspflege:</p>
    <div class="photo care__photo2" role="img" aria-label="Foto: Verbandsrollen und Klemme"></div>
    <ul class="checks care__list">
      <li>Krankenpflege nach §37.1 (Krankenhausnachsorge)</li>
      <li>Verabreichen und Richten von Medikamenten</li>
      <li>Verabreichen von Augentropfen</li>
      <li>Wundverbände anlegen und wechseln</li>
      <li>Wundversorgungen</li>
      <li>Dekubitusbehandlung</li>
      <li>Kompressionsstrümpfe an- und ausziehen</li>
      <li>Kompressionsverbände anlegen und abnehmen</li>
      <li>Blutdruckmessung</li>
      <li>Blutzucker messen</li>
      <li>Insulininjektionen</li>
      <li>Injektionen</li>
      <li>Infusionen</li>
      <li>Einläufe, Klistiere</li>
      <li>Einreibungen</li>
      <li>Stomabehandlung</li>
      <li>PEG Versorgung</li>
    </ul>
  </article>

  <article class="panel contact-panel">
    <div class="contact-panel__main">
      <div class="brand"><span class="brand__dot"></span>Pflegehaus Warnow</div>
      <ul class="contact">
        <li><svg width="12" height="12" viewBox="0 0 12 12"><path d="M6 1a3.5 3.5 0 0 0-3.5 3.5C2.5 7 6 11 6 11s3.5-4 3.5-6.5A3.5 3.5 0 0 0 6 1z" fill="#fff"/><circle cx="6" cy="4.5" r="1.3" fill="#93d27e"/></svg><span>Pflegehaus Warnow GmbH<br>Lindenweg 12 | 18055 Rostock</span></li>
        <li><svg width="12" height="12" viewBox="0 0 12 12"><path d="M2.5 1.5l2 .2 1 2.4-1.2 1a6 6 0 0 0 2.6 2.6l1-1.2 2.4 1 .2 2c-4.5.6-8.6-3.5-8-8z" fill="#fff"/></svg><span>Telefon:<br>0381-4402718</span></li>
        <li><svg width="12" height="12" viewBox="0 0 12 12"><rect x="1" y="2.5" width="10" height="7" rx="1" fill="#fff"/><path d="M1.5 3l4.5 3.5L10.5 3" stroke="#93d27e" fill="none"/></svg><span>E-Mail:<br>info@pflegehaus-warnow.de</span></li>
      </ul>
      <span class="pill pill--blue url">www.pflegehaus-warnow.de</span>
    </div>

    <div class="contact-panel__branch">
      <div class="brand"><span class="brand__dot"></span>MOVIKA</div>
      <p class="contact-panel__tag">Der Mobile Pflegedienst</p>
      <ul class="contact">
        <li><svg width="12" height="12" viewBox="0 0 12 12"><path d="M6 1a3.5 3.5 0 0 0-3.5 3.5C2.5 7 6 11 6 11s3.5-4 3.5-6.5A3.5 3.5 0 0 0 6 1z" fill="#fff"/><circle cx="6" cy="4.5" r="1.3" fill="#93d27e"/></svg><span>Filiale Gnoien<br>Feldstrasse 14 | 17179 Gnoien</span></li>
        <li><svg width="12" height="12" viewBox="0 0 12 12"><path d="M2.5 1.5l2 .2 1 2.4-1.2 1a6 6 0 0 0 2.6 2.6l1-1.2 2.4 1 .2 2c-4.5.6-8.6-3.5-8-8z" fill="#fff"/></svg><span>Telefon:<br>039971 206451</span></li>
        <li><svg width="12" height="12" viewBox="0 0 12 12"><rect x="1" y="2.5" width="10" height="7" rx="1" fill="#fff"/><path d="M1.5 3l4.5 3.5L10.5 3" stroke="#93d27e" fill="none"/></svg><span>E-Mail:<br>info@movika.de</span></li>
      </ul>
      <span class="pill pill--blue url">www.movika.de</span>
    </div>
  </article>

  <article class="panel cover">
    <div class="brand cover__brand"><span class="brand__dot"></span>Pflegehaus Warnow</div>
    <svg class="cover__band" viewBox="0 0 273 330" preserveAspectRatio="none" aria-hidden="true">
      <path d="M0 60 C60 110 200 110 273 20 L273 330 L0 330 Z" fill="var(--blue)"/>
      <path d="M0 60 C60 110 200 110 273 20" stroke="#d9e6f3" stroke-width="5" fill="none"/>
    </svg>
    <div class="photo cover__photo" role="img" aria-label="Foto: Pflegerin umarmt lächelnd eine ältere Dame"></div>
    <div class="badge cover__badge">Krankenkassen bezahlen die Leistungen für Sie</div>
    <h1 class="hand cover__title">Der Pflegedienst im Herzen von Rostock</h1>
    <span class="pill pill--orange url cover__url">www.pflegehaus-warnow.de</span>
  </article>
</section>

<section class="sheet sheet--inside">
  <article class="panel insulin">
    <div class="photo insulin__photo" role="img" aria-label="Foto: Insulinpen, Teststreifen und Blutzuckermessgerät"></div>
    <h2 class="pill pill--green section-title insulin__title">Insulininjektion</h2>
    <div class="insulin__text">
      <h3>Wir helfen Ihnen bei Insulin-Injektionen</h3>
      <p>Sollten Sie oder Ihre Angehörigen einen Hilfebedarf bei behandlungspflegerischen Leistungen haben, setzen wir uns gerne mit Ihrem Hausarzt in Verbindung. Dies ist selbstverständlich ein kostenloser Service des Mobilen Pflegedienstes PFLEGEHAUS-WARNOW.</p>
      <h3>Voraussetzungen sind:</h3>
      <ul class="checks">
        <li>Es muss eine behandlungsbedürftige Erkrankung vorliegen</li>
        <li>Ein Arzt muss eine Verordnung auf Behandlungspflege ausstellen</li>
        <li>Sie selbst oder eine Person in Ihrem Haushalt sind nicht in der Lage, die Leistung auszuführen, beispielsweise eine Insulininjektion oder das Anziehen von Kompressionsstrümpfen.</li>
      </ul>
      <p>Behandlungspflegen (z.B. Injektionen, Verbandswechsel) sind gleichzeitig neben Leistungen der Pflegeversicherung möglich. Wenn Sie Leistungen der Behandlungspflege in Anspruch nehmen, wird das Pflegegeld nicht gekürzt.</p>
    </div>
  </article>

  <article class="panel promise">
    <div class="brand promise__brand"><span class="brand__dot"></span>Pflegehaus Warnow</div>
    <div class="promise__slogan">
      <span class="pill pill--green">Pflege bedeutet</span>
      <span class="pill pill--green">Verantwortung!</span>
      <span class="pill pill--orange">Wir kümmern uns um Sie</span>
    </div>
    <span class="pill pill--blue promise__phone">
      <svg width="14" height="14" viewBox="0 0 12 12"><path d="M2.5 1.5l2 .2 1 2.4-1.2 1a6 6 0 0 0 2.6 2.6l1-1.2 2.4 1 .2 2c-4.5.6-8.6-3.5-8-8z" fill="#fff"/></svg>
      0800 3172 640 <small>(KOSTENFREI)</small>
    </span>
    <div class="photo promise__photo" role="img" aria-label="Foto: junge Hand hält die Hand einer älteren Person"></div>
  </article>

  <article class="panel stockings">
    <div class="photo stockings__photo" role="img" aria-label="Foto: Hände beim Anziehen eines Kompressionsstrumpfs"></div>
    <h2 class="pill pill--green section-title stockings__title">Kompressionsstrümpfe</h2>
    <div class="stockings__text">
      <h3>Wir helfen Ihnen beim Anziehen von Kompressionsstrümpfen</h3>
      <p>Unter dem Begriff „Behandlungspflege“ sind all diejenigen Tätigkeiten zusammengefasst, die zur Behandlung/Therapie einer Krankheit notwendig sind und durch Ihren Hausarzt verordnet werden.</p>
      <h3>Sie umfasst folgende Hilfeleistungen:</h3>
      <ul class="checks">
        <li>Die Gabe von Medikamenten</li>
        <li>An- und Ausziehen von Kompressionsstrümpfen</li>
        <li>Injektionen, Verbände, Wund- und Dekubitus Versorgung</li>
      </ul>
      <p>Die notwendigen verordneten und bewilligten Leistungen der Behandlungspflege werden von den Krankenkassen komplett finanziert bis auf die gesetzlich festgelegten Zahlungen.</p>
      <p>Wenn Sie von der Zahlung befreit sind, müssen Sie zur Behandlungspflege nichts zahlen.</p>
    </div>
  </article>
</section>

</body>
</html>
```